Business Card Design for Cybersecurity Company - Quorvent Systems

We need a business card design for our new cybersecurity company, Quorvent. We’re going for a clean, hi tech look that feels modern, premium, and trustworthy. We want a design that really stands out and makes people say WOW when we hand it over!

Quorvent delivers reliable IT support and managed services for small and mid sized businesses. We help companies stay secure, efficient, and connected through proactive monitoring, cybersecurity services, cloud management, and remote support.

Target Market(s)

Designers should target small and mid sized businesses that need dependable cybersecurity and IT support.

Industry/Entity Type

Cybersecurity, Managed Service Provider, IT services

Contact Information for Business Card

Contact information

Requirements
Must have
• The card should look clean, modern, and tech focused, with the Quorvent logo, clear contact info, and strong readability. It needs to feel premium and professional while still keeping a simple layout that fits a cybersecurity and IT brand.
Nice to have
• Nice to have elements include subtle touches that give the card a modern, tech feel, along with a layout that works well in different background styles.
Should not have
• The card should avoid clutter, loud graphics, or anything that takes attention away from the logo and contact details.

```html
<!DOCTYPE html>
<html lang="en">
<head>
<meta charset="UTF-8">
<title>Quorvent Systems – Business Card</title>
<link rel="stylesheet" href="https://fonts.googleapis.com/css2?family=Montserrat:wght@700&family=Roboto:wght@400;500&display=swap">
<style>
  :root {
    --stage: #c9c9c9;
    --card-black: #000000;
    --card-back: #141414;
    --ink: #ffffff;
    --brand-blue: #2f6df2;
    --brand-violet: #6a2bd9;
    --band-blue: #1f8bff;
    --rule: #cfcfcf;
    --emboss: #2a2a2a;
    --emboss-light: #333333;
  }
  html, body {
    margin: 0;
    width: 1200px;
    height: 802px;
    overflow: hidden;
    background: var(--stage);
    font-family: "Roboto", Arial, sans-serif;
  }
  .stage {
    position: relative;
    width: 1200px;
    height: 802px;
    display: flex;
    align-items: center;
    justify-content: center;
    gap: 40px;
  }
  .card {
    position: relative;
    width: 540px;
    height: 309px;
    border-radius: 22px;
    overflow: hidden;
    box-shadow: 0 14px 30px rgba(0,0,0,.35);
  }
  .card--front { background: var(--card-black); color: var(--ink); }
  .card--back { background: var(--card-back); }

  .brand {
    position: absolute;
    top: 44px;
    right: 70px;
    display: flex;
    align-items: center;
    gap: 12px;
  }
  .brand__mark {
    width: 26px;
    height: 26px;
    background: var(--brand-blue);
  }
  .brand__name {
    font-family: "Montserrat", Arial, sans-serif;
    font-weight: 700;
    font-size: 30px;
    color: var(--brand-blue);
    letter-spacing: .5px;
  }

  .person {
    position: absolute;
    left: 38px;
    top: 112px;
  }
  .person__name {
    font-family: "Montserrat", Arial, sans-serif;
    font-weight: 700;
    font-size: 24px;
    background: linear-gradient(90deg, var(--brand-violet), var(--brand-blue));
    -webkit-background-clip: text;
    background-clip: text;
    color: transparent;
    margin: 0;
  }
  .person__role {
    font-size: 14px;
    margin: 4px 0 0;
  }
  .rule {
    position: absolute;
    left: 38px;
    top: 172px;
    width: 420px;
    height: 1px;
    background: var(--rule);
  }
  .contact {
    position: absolute;
    top: 184px;
    display: grid;
    gap: 6px;
    font-size: 14px;
  }
  .contact--left { left: 38px; }
  .contact--right { left: 230px; }
  .contact__row { display: flex; align-items: center; gap: 8px; }
  .contact__icon { width: 14px; height: 14px; flex: none; }

  .address {
    position: absolute;
    right: 34px;
    top: 186px;
    font-size: 13px;
    line-height: 1.35;
    text-align: left;
  }
  .band {
    position: absolute;
    left: 0;
    bottom: 0;
    width: 540px;
    height: 52px;
  }
  .band__url {
    position: absolute;
    right: 40px;
    bottom: 9px;
    font-size: 14px;
    font-weight: 500;
    color: var(--ink);
  }

  .back-brand {
    position: absolute;
    inset: 0;
    display: flex;
    align-items: center;
    justify-content: center;
    gap: 16px;
  }
  .back-brand__mark {
    width: 40px;
    height: 40px;
    background: var(--emboss);
    box-shadow: 1px 1px 0 var(--emboss-light);
  }
  .back-brand__name {
    font-family: "Montserrat", Arial, sans-serif;
    font-weight: 700;
    font-size: 42px;
    color: var(--emboss);
  }
</style>
</head>
<body>
<main class="stage">
  <section class="card card--front" aria-label="Business card front">
    <div class="brand">
      <span class="brand__mark"></span>
      <span class="brand__name">Quorvent Systems</span>
    </div>

    <div class="person">
      <h1 class="person__name">Dana Whitcombe</h1>
      <p class="person__role">Owner | CEO | Quorvent Systems</p>
    </div>

    <div class="rule"></div>

    <div class="contact contact--left">
      <div class="contact__row">
        <svg class="contact__icon" viewBox="0 0 16 16"><path d="M3 1l3 3-2 2c1 2 3 4 6 6l2-2 3 3-2 2C7 15 1 9 1 3z" fill="#7a3df0"/></svg>
        <span>(855) 430-QUOR</span>
      </div>
      <div class="contact__row">
        <svg class="contact__icon" viewBox="0 0 16 16"><rect x="4" y="1" width="8" height="14" rx="1.5" fill="none" stroke="#2f6df2" stroke-width="1.6"/><circle cx="8" cy="12.5" r="1" fill="#2f6df2"/></svg>
        <span>(813) 555-0192</span>
      </div>
    </div>

    <div class="contact contact--right">
      <div class="contact__row">
        <svg class="contact__icon" viewBox="0 0 16 16"><path d="M3 1l3 3-2 2c1 2 3 4 6 6l2-2 3 3-2 2C7 15 1 9 1 3z" fill="#3a5cf0"/></svg>
        <span>(855) 430 7781</span>
      </div>
      <div class="contact__row">
        <svg class="contact__icon" viewBox="0 0 16 16"><rect x="1" y="3" width="14" height="10" fill="#5a3ef0"/><path d="M1 3l7 6 7-6" fill="none" stroke="#000" stroke-width="1.2"/></svg>
        <span>dana@quorvent.com</span>
      </div>
    </div>

    <address class="address" style="font-style:normal">PO Box 51820,<br>Lakemont, FL 33790</address>

    <svg class="band" viewBox="0 0 540 52" preserveAspectRatio="none" aria-hidden="true">
      <defs>
        <linearGradient id="bandGrad" x1="0" y1="0" x2="1" y2="0">
          <stop offset="0" stop-color="#7a22d6"/>
          <stop offset=".55" stop-color="#3a5cf0"/>
          <stop offset="1" stop-color="#1f8bff"/>
        </linearGradient>
      </defs>
      <path d="M0 36 L290 36 Q300 36 304 28 L310 18 Q314 14 322 14 L540 14 L540 52 L0 52 Z" fill="url(#bandGrad)"/>
      <path d="M0 36 L290 36 Q300 36 304 28 L308 21 L300 21 Q296 28 288 30 L0 30 Z" fill="#ffffff"/>
    </svg>
    <span class="band__url">www.quorvent.com</span>
  </section>

  <section class="card card--back" aria-label="Business card back">
    <div class="back-brand">
      <span class="back-brand__mark"></span>
      <span class="back-brand__name">Quorvent Systems</span>
    </div>
  </section>
</main>
</body>
</html>
```